Vornexa Ad Banners for Car Buying Service

We offer a fast, safe way for car owners to sell their car. They load the car details on our site, we give them a cash offer. If interested, we visit them and conclude deal, same day payment.
I want subtle animated banners for our Vornexa Display ads. (Dimensions - 120x600 - 160x600 - 300x250 - 300x600 - 320 x 50 - 728x90)
We can discuss messaging. I will attach recent static banners we had designed - and an older HTML5 animated version.
I'm looking for something subtle, modern but with clear call to action.
Target Market(s)
Car owners, male and female - wanting an easy, no fuss way to sell their car for cash
Industry/Entity Type
Automotive

```html
<!DOCTYPE html>
<html lang="en">
<head>
<meta charset="utf-8">
<title>Motorvale – We Want Your Car More</title>
<link href="https://fonts.googleapis.com/css2?family=Poppins:wght@700;800&display=swap" rel="stylesheet">
<style>
  :root {
    --sky-top: #03a2e2;
    --sky-bottom: #00668f;
    --ink: #0a0a0a;
    --paper: #ffffff;
    --brand-blue: #039fe0;
    --olive: #a1ab45;
    --silver-light: #f2f3f4;
    --silver-dark: #9c9fa3;
    --logo-ink: #141414;
  }
  html, body {
    margin: 0;
    padding: 0;
    width: 1200px;
    height: 794px;
    overflow: hidden;
  }
  .banner {
    width: 1200px;
    height: 794px;
    background: linear-gradient(180deg, var(--sky-top) 0%, var(--sky-bottom) 100%);
  }
  .banner-art {
    display: block;
    width: 1200px;
    height: 794px;
  }
  .headline {
    font-family: "Poppins", sans-serif;
    font-weight: 800;
    font-size: 128px;
    fill: var(--paper);
  }
  .headline .accent-blue { fill: var(--brand-blue); }
  .headline .accent-olive { fill: var(--olive); }
  .brand-name {
    font-family: "Poppins", sans-serif;
    font-weight: 700;
    font-size: 112px;
    fill: var(--logo-ink);
  }
</style>
</head>
<body>
  <main class="banner">
    <svg class="banner-art" viewBox="0 0 2370 1568" preserveAspectRatio="none" xmlns="http://www.w3.org/2000/svg">
      <defs>
        <linearGradient id="silver-fill" x1="0" y1="0" x2="1" y2="1">
          <stop offset="0" stop-color="var(--silver-dark)"/>
          <stop offset="0.45" stop-color="var(--silver-light)"/>
          <stop offset="1" stop-color="var(--silver-dark)"/>
        </linearGradient>
        <clipPath id="panel-clip">
          <rect x="140" y="262" width="2090" height="1043" rx="50"/>
        </clipPath>
      </defs>

      <g class="panel" clip-path="url(#panel-clip)">
        <rect class="panel-base" x="140" y="262" width="2090" height="1043" fill="var(--ink)"/>
        <path class="wave-blue" fill="var(--brand-blue)"
          d="M148,285 C230,420 300,505 500,515 L1760,520 C2000,540 2180,700 2230,890 L2230,965 C2150,760 2000,620 1800,620 L1430,642 L330,650 C250,600 200,450 148,285 Z"/>
        <path class="wave-white" fill="var(--paper)"
          d="M140,285 C200,560 230,640 330,650 L1430,642 L1800,620 C2000,620 2150,760 2230,965 L2230,1292 C2150,1140 2080,1085 1800,1080 L480,1078 C300,1075 235,1000 200,870 L140,675 Z"/>
      </g>

      <text class="headline" x="318" y="430" textLength="1732" lengthAdjust="spacingAndGlyphs">WE DO <tspan class="accent-blue">MORE</tspan> WE HELP <tspan class="accent-blue">MORE</tspan></text>

      <rect class="car-photo" role="img" aria-label="Top-down photo of a silver sedan"
        x="265" y="530" width="1175" height="460" rx="200" fill="url(#silver-fill)"/>

      <text class="brand-name" x="1510" y="968" textLength="620" lengthAdjust="spacingAndGlyphs">Motorvale.co.za</text>

      <text class="headline" x="318" y="1237" textLength="1672" lengthAdjust="spacingAndGlyphs">WE WANT <tspan class="accent-olive">YOUR</tspan> CAR <tspan class="accent-olive">MORE</tspan></text>
    </svg>
  </main>
</body>
</html>
```